Postcard designed to acquire new customers

Need a postcard style AD to place in dentist offices and other professionals to promote our tax saving system. We will place these in dentists offices, orthodontist, optometrist, physiotherapist and all sorts of medical/dental offices. The card should highlight how they can save taxes by using our software. Our website has good information on it, and I'll include the advertising PDF that our software company produces. Our logo is a little out-dated and I've included the bonus of the winner re-making the logo so its better than it currently is.
Updates

I don't need to have any space allocated for a stamp and address. We are using this to place in offices and are for advertising purposes, not mailing. Thanks!

Reason: My apologies for not providing feedback yet, I've lost several days due to some illness and am finally back at work. I'll be going through designs today and would like the extra few days to work with many of you to create a great design. Thank you for your patience! Dalmon

Reason: Again, my apologies for the delay. I will be in contact with designers this week. Thank you,

Target Market(s)

Small Business Owners in Canada

Industry/Entity Type

Health Insurance

Logo Text

Save Time, Save Money

Other font styles liked:
• Easy to Read Font's

Colors

Designer to choose colors to be used in the design.

Requirements
Must have
• Must have a call to action on the postcard to sell the service. We need people to have their attention caught. A call to action could be, "You're spending too much on taxes! That's what they'll say if your business doesn't have a Kivo Health Spending Account..."
• See the PDF for other catch phrases or key information on what a Health Spending Account is. Many people don't know so I'd like to see 3-4 bullet points on the front of the postcard on what a health spending account is. See the attached PDF for that information and simplifying the information to short bullet points would be best. Here are my thoughts:
• Who should have a Kivo Health Spending Account?
• - Every business owner who is incorporated should have one.
• - Write off 100% of this ZWK approved this method.
• - It is the most tax effective way to run dental, health, vision and other expenses through your company.
• - Easy to use APP for your phone, 2-day turnaround time for claims
• If you aren't using this, you're throwing tax dollars away!
• The back of the postcard would include 2 things. First, an example of the taxes you can save, and second - the different information they can send us so we can setup your account.
• First is the example of how this saves you money. Assuming a 38% personal tax rate. You will need to earn $1.62 of gross income, pay $0.62 of personal tax, which leaves you with $1.00 of after tax money to use for your personal expenses.
• The example of using a Kivo Health Spending Account, or doing nothing would need the following information.
• Comparison
• $5,000 of medical, dental, vision expenses
• Do Nothing Kivo Health Spending Account
• $8,100 – Total Cost $5,525 – Total Cost
• $3,100 – Income Tax $500 fee & $25 GST
• $5,000 – Money needed for medical, dental, vision, etc. $5,000 – Money needed for medical, dental, vision, etc.
• SAVINGS is $2,575
• Assuming a company incorporated in Alberta and a one time setup fee of $275 has not been included in the comparison.
• Information to send us to setup your account is:
• - Names and birth dates of you and your dependents
• - Contact information for you and your business (if different) Address, email, phone numbers
• - We will contact you about how to setup the app, your banking details and some other items.
• - Setup fee is a one-time payment of $275
Nice to have
• I'd like the front of the postcard to not be very busy with the background or graphics, etc. I want the call to action to be very obvious so they want to read the bullet points and look at the back of the postcard for more information.

```html
<!DOCTYPE html>
<html lang="en">
<head>
<meta charset="utf-8">
<title>Kivo Health Spending Account – Postcard</title>
<link href="https://fonts.googleapis.com/css2?family=Oswald:wght@400;500;700&family=Lato:wght@400;700&display=swap" rel="stylesheet">
<style>
  :root{
    --ink:#1a1a1a;
    --dark:#141414;
    --orange:#f04e1c;
    --blue:#243a9c;
    --navy:#1f2f8a;
    --green:#2a9a3c;
    --red:#d2381f;
    --paper:#f1f1f1;
    --text:#2b2b2b;
    --teal:#1fa7b8;
  }
  *{box-sizing:border-box;margin:0;padding:0}
  html,body{width:1200px;height:1200px;overflow:hidden}
  body{background:#e4e4e4;font-family:"Lato",sans-serif;color:var(--text);position:relative}
  .card{position:absolute;left:159px;width:882px;height:570px;overflow:hidden;box-shadow:0 2px 10px rgba(0,0,0,.25)}
  .card--front{top:15px;background:var(--dark)}
  .card--back{top:610px;background:var(--paper);display:flex}

  /* FRONT */
  .front-photo{position:absolute;left:0;top:0;width:460px;height:467px;
    background:radial-gradient(ellipse at 35% 55%,#8a8a8a 0%,#4a4a4a 35%,#1e1e1e 70%,var(--dark) 100%)}
  .front-copy{position:absolute;left:355px;top:10px;right:16px;color:#fff;font-family:"Oswald",sans-serif}
  .kicker{font-size:26px;font-weight:400;line-height:1.05}
  .headline{font-size:57px;font-weight:700;color:var(--orange);line-height:1;letter-spacing:.5px;padding-bottom:6px;border-bottom:1px solid #8c8c8c}
  .subline{font-size:25px;font-weight:400;line-height:1.35;margin-top:8px}
  .account-band{position:absolute;left:283px;top:190px;width:599px;height:52px;background:var(--blue);
    color:#fff;font-family:"Oswald",sans-serif;font-weight:700;font-size:29px;line-height:52px;padding-left:72px}
  .who{position:absolute;left:480px;top:254px;right:14px;color:#fff}
  .who h3{font-family:"Oswald",sans-serif;font-weight:500;font-size:15px;text-align:right;margin-bottom:14px}
  .who ul{list-style:none}
  .who li{display:flex;gap:20px;font-size:13.5px;line-height:1.3;margin-bottom:18px}
  .who li svg{flex:0 0 14px;margin-top:1px}
  .front-strip{position:absolute;left:0;bottom:0;width:100%;height:103px;
    background:linear-gradient(90deg,#dcdcdc,#f4f4f4 50%,#e2e2e2);border-top:2px solid var(--blue);display:flex;align-items:center}
  .brand{width:355px;padding-left:20px}
  .brand-name{display:flex;align-items:center;gap:8px;font-family:"Lato",sans-serif;font-size:22px;font-weight:700;color:var(--ink)}
  .brand-name i{width:14px;height:14px;background:var(--blue);display:inline-block}
  .warning{font-family:"Oswald",sans-serif;font-size:29px;line-height:1.2;color:var(--navy)}
  .warning strong{font-weight:700}
  .warning .green{color:var(--green)}

  /* BACK */
  .savings{width:505px;padding:14px 0 0 14px;border-right:3px solid #c9c9c9;background:#f5f5f5}
  .savings h2{font-family:"Oswald",sans-serif;font-weight:400;font-size:24px;color:var(--ink);display:inline-block;border-bottom:1.5px solid var(--navy);line-height:1.1;margin-bottom:10px}
  .savings h2 strong{color:var(--navy);font-weight:700}
  .savings p{font-size:15px;line-height:1.4;padding-right:12px;margin-bottom:10px;text-align:justify}
  .savings p b{color:var(--navy);font-size:18px;font-weight:700}
  .compare-title{font-family:"Oswald",sans-serif;font-weight:700;font-size:15px;text-decoration:underline;margin:2px 0 12px}
  .compare{width:491px;border-collapse:collapse;font-size:15px}
  .compare td{height:26px;padding:0 16px;white-space:nowrap}
  .compare .band td{background:var(--green);color:#fff}
  .compare .light td{background:#fff;color:var(--ink)}
  .compare .r{color:var(--red)}
  .notes{list-style:none;margin-top:16px}
  .notes li{position:relative;padding-left:22px;font-size:15px;line-height:1.35;margin-bottom:10px;padding-right:20px}
  .notes li::before{content:"";position:absolute;left:0;top:5px;width:10px;height:10px;background:var(--red)}
  .notes li b{color:var(--navy);font-size:18px}
  .notes .narrow{padding-right:200px}

  .signup{flex:1;padding:26px 14px 0 30px;background:linear-gradient(160deg,#f7f7f7,#e9e9e9)}
  .signup .brand{width:auto;padding:0;margin-bottom:24px}
  .signup .brand-name{justify-content:center;font-size:24px}
  .form-row{display:flex;align-items:flex-end;font-size:15px;font-weight:700;color:var(--ink);height:32px}
  .form-row span{flex:1;border-bottom:1.5px solid #555;margin-left:4px;height:14px}
  .phones{display:flex;justify-content:center;gap:26px;margin:20px 0 14px}
  .phone{width:76px;height:146px;border-radius:10px;background:#202020;padding:14px 5px}
  .phone div{width:100%;height:100%;background:linear-gradient(180deg,#e8f6f8 0%,#e8f6f8 30%,var(--teal) 30%,#178a99 100%)}
  .contacts{display:grid;grid-template-columns:170px 1fr;row-gap:8px;font-size:13px;color:var(--ink)}
  .contacts div{display:flex;align-items:center;gap:8px}
  .contacts .big{font-size:17px}
</style>
</head>
<body>

<section class="card card--front">
  <div class="front-photo" role="img" aria-label="Photo of a hand dropping a coin into a white piggy bank beside stacks of coins on a wooden table"></div>
  <div class="front-copy">
    <div class="kicker">YOU'RE SPENDING</div>
    <div class="headline">TOO MUCH ON TAXES!</div>
    <div class="subline">THAT'S WHAT THEY'LL SAY IF YOUR BUSINESS<br>DOESN'T HAVE A</div>
  </div>
  <div class="account-band">KIVO HEALTH SPENDING ACCOUNT...</div>
  <div class="who">
    <h3>WHO SHOULD HAVE A KIVO HEALTH SPENDING ACCOUNT?</h3>
    <ul>
      <li><svg width="14" height="14" viewBox="0 0 14 14"><rect x="1" y="3" width="10" height="10" fill="none" stroke="#fff" stroke-width="1.4"/><path d="M3 7l3 3 7-8" fill="none" stroke="#fff" stroke-width="1.8"/></svg>Every business owner who is incorporated should have one.</li>
      <li><svg width="14" height="14" viewBox="0 0 14 14"><rect x="1" y="3" width="10" height="10" fill="none" stroke="#fff" stroke-width="1.4"/><path d="M3 7l3 3 7-8" fill="none" stroke="#fff" stroke-width="1.8"/></svg>Write off 100% of this ZWK approved this method.</li>
      <li><svg width="14" height="14" viewBox="0 0 14 14"><rect x="1" y="3" width="10" height="10" fill="none" stroke="#fff" stroke-width="1.4"/><path d="M3 7l3 3 7-8" fill="none" stroke="#fff" stroke-width="1.8"/></svg>It is the most tax effective way to run dental, health, vision and other expenses through your company.</li>
      <li><svg width="14" height="14" viewBox="0 0 14 14"><rect x="1" y="3" width="10" height="10" fill="none" stroke="#fff" stroke-width="1.4"/><path d="M3 7l3 3 7-8" fill="none" stroke="#fff" stroke-width="1.8"/></svg>Easy to use APP for your phone, 2-day turnaround time for claims</li>
    </ul>
  </div>
  <div class="front-strip">
    <div class="brand">
      <div class="brand-name"><i></i>Kivo Health</div>
    </div>
    <div class="warning">IF YOU AREN'T USING THIS<br><strong>YOU'RE <span class="green">THROWING TAX DOLLARS</span> AWAY!</strong></div>
  </div>
</section>

<section class="card card--back">
  <div class="savings">
    <h2>HOW TO <strong>SAVE YOUR MONEY</strong></h2>
    <p>Assuming a <b>38%</b> personal tax rate. You will need to earn <b>$1.62</b> of gross income, pay <b>$0.62</b> of personal tax, which leaves you with <b>$1.00</b> of after tax money to use for your personal expenses.</p>
    <p>The example of using a Kivo Health Spending Account, or doing nothing would need the following information.</p>
    <div class="compare-title">COMPARISON</div>
    <table class="compare">
      <tr class="band"><td>$5,000 of medical, dental, vision expenses</td></tr>
      <tr class="light"><td>Do Nothing &nbsp;Kivo Health Spending Account</td></tr>
      <tr class="band"><td>$8,100 – Total Cost &nbsp;&nbsp;&nbsp;$5,525 – Total Cost</td></tr>
      <tr class="light"><td><span class="r">$3,100</span> – &nbsp;Income Tax &nbsp;<span class="r">$500</span> fee &amp; <span class="r">$25</span> GST</td></tr>
      <tr class="band"><td>$5,000 – Money needed for medical, dental, vision, etc.</td></tr>
      <tr class="light"><td>SAVINGS is - <span class="r">$2,575</span></td></tr>
    </table>
    <ul class="notes">
      <li>Assuming a company incorporated in Alberta and a one time setup fee of <b>$275</b> has not been included in the comparison.</li>
      <li class="narrow">We will contact you about how to setup the app, your banking details and some other items.</li>
      <li>Setup fee is a one-time payment of <b>$275</b></li>
    </ul>
  </div>
  <div class="signup">
    <div class="brand">
      <div class="brand-name"><i></i>Kivo Health</div>
    </div>
    <div class="form-row">Names<span></span></div>
    <div class="form-row">Date of Birth<span></span></div>
    <div class="form-row">Your Dependents<span></span></div>
    <div class="form-row">Email<span></span></div>
    <div class="form-row">Phone Numbers<span></span></div>
    <div class="form-row">Address<span></span></div>
    <div class="phones">
      <div class="phone" role="img" aria-label="Phone showing the app welcome and balance screen"><div></div></div>
      <div class="phone" role="img" aria-label="Phone showing the app receipt upload screen"><div></div></div>
      <div class="phone" role="img" aria-label="Phone showing the app make a claim form"><div></div></div>
    </div>
    <div class="contacts">
      <div class="big"><svg width="16" height="16" viewBox="0 0 16 16"><path d="M3 2l3 0 1 3-2 1.5a8 8 0 0 0 4.5 4.5L11 9l3 1v3c0 1-1 1.5-2 1.5A11 11 0 0 1 1.5 4C1.5 3 2 2 3 2z" fill="var(--red)"/></svg>555-014-2290</div>
      <div><svg width="16" height="14" viewBox="0 0 16 14"><rect x="1" y="1" width="14" height="12" fill="var(--red)"/><path d="M1 1l7 6 7-6" fill="none" stroke="#fff" stroke-width="1.3"/></svg>hello@kivohealth.ca</div>
      <div><svg width="16" height="16" viewBox="0 0 16 16"><circle cx="8" cy="8" r="7" fill="none" stroke="var(--red)" stroke-width="1.4"/><path d="M1 8h14M8 1c-3 3-3 11 0 14M8 1c3 3 3 11 0 14" fill="none" stroke="var(--red)" stroke-width="1.2"/></svg>www.kivohealth.ca</div>
      <div><svg width="16" height="16" viewBox="0 0 16 16"><path d="M8 1l7 7h-2v7H9v-4H7v4H3V8H1z" fill="var(--red)"/></svg>your address here</div>
    </div>
  </div>
</section>

</body>
</html>
```